Pelmora, The winning solution for fundraising

Pelmora needs a simple Wordpress website development. The key message is that we have three wins in fundraising according to my services - win for theorganisation - win for the partner and win for the audience and the community.STYLE:- My business card is attached so the site colors could match with the card;- We love the style of this website: https://www.marnacovestel.co.nz/ because it is modern, minimalist, clean and easy to navigate. I am happy to have a similar parallax (scrolling) site as the reference samplePlease feature the following on the site:* INTRODUCTION (or About)* SERVICES* MY QUOTE* CONTACT US* LINKEDIN ( the contents are in the attached .rtf file - please message me if you are unable to open this document)Deliverables:- I would like a fully functioning (Coded) wordpress site

• Personable approach
• It is all about You (the other person who is approach my business)

```html
<!DOCTYPE html>
<html lang="en">
<head>
<meta charset="utf-8">
<title>Pelmora</title>
<link href="https://fonts.googleapis.com/css2?family=Poppins:wght@300;400;500;600;700&family=Roboto:wght@400;500&display=swap" rel="stylesheet">
<style>
:root{
  --rose:#c08878;
  --rose-dark:#a8705f;
  --ink:#222;
  --navy:#191330;
  --navy-2:#2b1d45;
  --footer:#2c2c30;
  --line:#e6e6e6;
  --white:#fff;
}
*{box-sizing:border-box;margin:0;padding:0}
html,body{width:1200px;height:4445px;overflow:hidden}
body{position:relative;font-family:"Poppins",sans-serif;color:var(--ink);background:var(--white)}
.abs{position:absolute}
/* header */
.site-header{position:absolute;left:0;top:0;width:1200px;height:148px;background:var(--white)}
.brand{left:90px;top:34px;font-size:62px;font-weight:400;line-height:1;color:#222}
.call{left:613px;top:22px;display:flex;gap:10px;align-items:center}
.call-text{font-size:15px;line-height:1.3}
.call-text b{color:var(--rose);font-weight:500;display:block;font-size:14px}
.search{left:858px;top:22px;width:247px;height:44px;border:1px solid #ddd;border-radius:22px;font-size:14px;color:#999;padding:12px 16px}
.search-btn{position:absolute;right:6px;top:7px;width:30px;height:30px;border-radius:50%;background:var(--rose)}
.main-nav{left:383px;top:104px;display:flex;gap:31px;font-size:17px;color:#222}
.social-top{left:990px;top:106px;display:flex;gap:14px}
.social-top span{width:14px;height:14px;border-radius:50%;background:#222}
/* hero */
.hero{left:0;top:148px;width:1200px;height:724px;background:linear-gradient(100deg,#1d3a4a 0%,#35627a 35%,#6a7d88 60%,#2e2a2a 100%)}
.hero-title{left:90px;top:330px;font-size:47px;font-weight:400;color:#fff;letter-spacing:-.5px}
.hero-title b{font-weight:600}
.hero-list{left:90px;top:408px;list-style:none;color:#fff;font-family:"Roboto",sans-serif;font-size:22px}
.hero-list li{height:45px;display:flex;align-items:center;gap:14px}
.hero-list li::before{content:"";width:12px;height:12px;border:3px solid #fff;border-radius:50%;box-shadow:inset 0 0 0 2px transparent}
.btn{display:flex;align-items:center;justify-content:center;gap:10px;background:var(--rose);color:#222;font-weight:600;border-radius:30px;font-size:18px}
.hero-btn{left:90px;top:560px;width:197px;height:53px}
.arrow{width:16px;height:16px;border-radius:50%;background:#222;position:relative}
.arrow::after{content:"";position:absolute;left:4px;top:5px;border-left:7px solid var(--rose);border-top:3px solid transparent;border-bottom:3px solid transparent}
/* services */
.section-title{width:1200px;left:0;text-align:center;font-size:36px;font-weight:600;color:#222}
.section-title span{color:var(--rose)}
.services-intro{left:130px;top:1058px;width:940px;text-align:center;font-family:"Roboto",sans-serif;font-size:16px;line-height:33px}
.card-img{width:331px;height:224px}
.card{width:297px;height:143px;background:#fff;border:1px solid #e2e2e2;box-shadow:0 2px 4px rgba(0,0,0,.08);text-align:center;padding-top:20px}
.card h3{font-size:21px;font-weight:500;margin-bottom:10px}
.card p{font-family:"Roboto",sans-serif;font-size:12px;line-height:25px;padding:0 10px}
.dots{left:566px;top:1878px;display:flex;gap:9px}
.dots span{width:16px;height:16px;border-radius:50%;background:var(--rose)}
.dots span:first-child{background:#fff;border:2px solid var(--rose);box-shadow:inset 0 0 0 3px #fff, inset 0 0 0 8px var(--rose)}
/* about */
.about{left:0;top:2024px;width:1200px;height:820px;background:radial-gradient(ellipse at 60% 35%,#3a2450 0%,var(--navy) 60%,#120e22 100%)}
.about-photo{left:81px;top:2214px;width:442px;height:442px;border-radius:50%;background:radial-gradient(circle at 45% 45%,#d8b487,#8e6a52 60%,#3d3b46);border:6px solid var(--rose)}
.about-title{left:560px;top:2255px;font-size:36px;font-weight:600;color:#fff}
.about-text{left:560px;top:2307px;width:550px;font-family:"Roboto",sans-serif;font-size:15.5px;line-height:36px;color:#fff;text-align:justify}
.about-text p+p{margin-top:9px}
.about-btn{left:560px;top:2547px;width:205px;height:54px}
/* quote */
.quote-mark{left:0;width:1200px;top:3030px;text-align:center;font-size:90px;line-height:1;color:var(--rose);font-family:Georgia,serif;font-weight:700;height:50px;overflow:hidden}
.quote-text{left:150px;top:3088px;width:900px;text-align:center;font-family:"Roboto",sans-serif;font-size:21px;line-height:40px}
.divider{left:155px;top:3219px;width:890px;height:1px;background:#ccc}
/* contact */
.contact-icon{width:86px;height:86px;border-radius:50%;background:var(--rose);display:flex;align-items:center;justify-content:center}
.contact-info{width:300px;text-align:center;font-size:16px;line-height:29px}
.field{height:42px;border:1px solid var(--line);box-shadow:0 2px 3px rgba(0,0,0,.08);font-size:12px;color:#666;padding:13px 16px}
.submit{left:516px;top:3784px;width:197px;height:60px;font-size:18px;box-shadow:0 3px 6px rgba(0,0,0,.2)}
/* footer */
.footer{left:0;top:3972px;width:1200px;height:473px;background:linear-gradient(180deg,#3a3a40,#1f1f22)}
.footer-brand{left:0;width:1200px;top:4150px;text-align:center;font-size:54px;font-weight:500;color:#fff}
.footer-social{left:528px;top:4236px;display:flex;gap:6px}
.footer-social span{width:30px;height:30px;border-radius:50%;border:2px solid #fff}
.footer-nav{left:0;width:1200px;text-align:center;color:#fff;font-size:17px;font-weight:500}
.footer-nav i{font-style:normal;margin:0 10px}
.copy{left:0;width:1200px;top:4382px;text-align:center;color:#ddd;font-size:15px}
</style>
</head>
<body>

<header class="site-header">
  <div class="abs brand">Pelmora</div>
  <div class="abs call">
    <svg width="40" height="40" viewBox="0 0 40 40"><circle cx="20" cy="20" r="18" fill="none" stroke="#c08878" stroke-width="2.5"/><path d="M13 12c2-2 4 2 5 4s-2 3-1 5 3 4 5 4 3-3 5-1 4 3 2 5-8 1-12-4-6-11-4-13z" fill="#c08878"/></svg>
    <div class="call-text"><b>CALL US:</b>(800) 555-0142</div>
  </div>
  <div class="abs search">Search<span class="search-btn"></span></div>
  <nav class="abs main-nav"><span>HOME</span><span>ABOUT US</span><span>OUR SERVICES</span><span>MY QUOTE</span><span>CONTACT US</span></nav>
  <div class="abs social-top"><span></span><span></span><span></span><span></span></div>
</header>

<section class="abs hero" role="img" aria-label="Man at a desk studying rising financial charts on a screen"></section>
<svg class="abs" style="left:0;top:780px" width="1200" height="95" viewBox="0 0 1200 95">
  <path d="M0 95 L0 85 Q600 -20 1200 85 L1200 95 Z" fill="#3b2c2c"/>
  <path d="M0 95 L0 92 Q600 5 1200 92 L1200 95 Z" fill="#fff"/>
</svg>
<h1 class="abs hero-title">WELCOME TO <b>PELMORA</b></h1>
<ul class="abs hero-list">
  <li>win for the organisation</li>
  <li>win for the partner</li>
  <li>win for the audience and the community.</li>
</ul>
<div class="abs btn hero-btn">Contact Us <span class="arrow"></span></div>

<h2 class="abs section-title" style="top:990px">OUR <span>SERVICES</span></h2>
<p class="abs services-intro">Sed ut perspiciatis unde omnis iste natus error sit voluptatem accusantium doloremque laudantium, totam rem aperiam, eaque ipsa quae ab illo inventore veritatis et quasi architecto beatae vitae dicta sunt explicabo.</p>

<div class="abs card-img" style="left:78px;top:1152px;background:linear-gradient(135deg,#5a5550,#b9a89a)" role="img" aria-label="Team planning marketing with notes on a table"></div>
<div class="abs card-img" style="left:435px;top:1152px;background:linear-gradient(160deg,#c4d4e8,#6a8bbf)" role="img" aria-label="Speaker presenting a fundraising workshop"></div>
<div class="abs card-img" style="left:793px;top:1152px;background:linear-gradient(135deg,#e9e2d0,#3a3a40)" role="img" aria-label="Laptop showing a funding screen on a desk"></div>
<div class="abs card" style="left:95px;top:1342px"><h3>Marketing Plans</h3><p>Sed ut perspiciatis unde omnis iste natus error sit voluptatem accusantium doloremque laudantium eaque veritatis vitae dicta sunt explicabo.</p></div>
<div class="abs card" style="left:452px;top:1342px"><h3>Workshops on Fundraising</h3><p>Sed ut perspiciatis unde omnis iste natus error sit voluptatem accusantium doloremque laudantium eaque veritatis vitae dicta sunt explicabo.</p></div>
<div class="abs card" style="left:810px;top:1342px"><h3>Funding applications</h3><p>Sed ut perspiciatis unde omnis iste natus error sit voluptatem accusantium doloremque laudantium eaque veritatis vitae dicta sunt explicabo.</p></div>

<div class="abs card-img" style="left:78px;top:1515px;background:linear-gradient(135deg,#e8e8e6,#5c5c5c)" role="img" aria-label="Seminar room with attendees facing a presenter"></div>
<div class="abs card-img" style="left:435px;top:1515px;background:linear-gradient(135deg,#3a4552,#1d232a)" role="img" aria-label="Colleagues meeting around a laptop"></div>
<div class="abs card-img" style="left:793px;top:1515px;background:linear-gradient(135deg,#b88a58,#6e5a48)" role="img" aria-label="Reports and charts spread on a wooden table"></div>
<div class="abs card" style="left:95px;top:1705px"><h3>Giving Programmes</h3><p>Sed ut perspiciatis unde omnis iste natus error sit voluptatem accusantium doloremque laudantium eaque veritatis vitae dicta sunt explicabo.</p></div>
<div class="abs card" style="left:452px;top:1705px"><h3>Legacy Programmes</h3><p>Sed ut perspiciatis unde omnis iste natus error sit voluptatem accusantium doloremque laudantium eaque veritatis vitae dicta sunt explicabo.</p></div>
<div class="abs card" style="left:810px;top:1705px"><h3>Feasibility Studies</h3><p>Sed ut perspiciatis unde omnis iste natus error sit voluptatem accusantium doloremque laudantium eaque veritatis vitae dicta sunt explicabo.</p></div>
<div class="abs dots"><span></span><span></span><span></span></div>

<section class="abs about"></section>
<svg class="abs" style="left:0;top:2024px" width="1200" height="90" viewBox="0 0 1200 90">
  <path d="M0 0 L1200 0 L1200 8 Q600 110 0 8 Z" fill="#3b2c2c"/>
  <path d="M0 0 L1200 0 L1200 5 Q600 90 0 5 Z" fill="#fff"/>
</svg>
<svg class="abs" style="left:0;top:2754px" width="1200" height="90" viewBox="0 0 1200 90">
  <path d="M0 90 L0 82 Q600 -20 1200 82 L1200 90 Z" fill="#3b2c2c"/>
  <path d="M0 90 L0 86 Q600 0 1200 86 L1200 90 Z" fill="#fff"/>
</svg>
<div class="abs about-photo" role="img" aria-label="Portrait of the consultant with long blonde hair"></div>
<h2 class="abs about-title">ABOUT US</h2>
<div class="abs about-text">
  <p>I come from Greece where I completed my Bachelor in Political Science and International Studies. I continued my studies in UK, in Birmingham where I received a Master's Degree in Diplomacy.</p>
  <p>Further education includes Mara Tennick courses, Institute of Board Leaders' governance courses, University of Westhaven Contract's Law and a 2017 Calder University paper on 'Disruptive Strategy'.</p>
</div>
<div class="abs btn about-btn">Read More <span class="arrow"></span></div>

<h2 class="abs section-title" style="top:2960px">MY QUOTE</h2>
<div class="abs quote-mark">&ldquo;</div>
<p class="abs quote-text">“ I look forward to working with you and your team andtogether achieving results that will make a difference where we live. ”</p>
<div class="abs divider"></div>

<h2 class="abs section-title" style="top:3266px">CONTACT US</h2>
<div class="abs contact-icon" style="left:230px;top:3364px"><svg width="44" height="32" viewBox="0 0 44 32"><rect x="1" y="1" width="42" height="30" fill="none" stroke="#fff" stroke-width="2"/><path d="M1 1 L22 18 L43 1 M1 31 L16 14 M43 31 L28 14" fill="none" stroke="#fff" stroke-width="2"/></svg></div>
<div class="abs contact-icon" style="left:572px;top:3364px"><svg width="34" height="46" viewBox="0 0 34 46"><path d="M17 40 C8 28 5 22 5 16 A12 12 0 0 1 29 16 C29 22 26 28 17 40Z" fill="none" stroke="#fff" stroke-width="2"/><circle cx="17" cy="16" r="5" fill="none" stroke="#fff" stroke-width="2"/><ellipse cx="17" cy="42" rx="12" ry="3" fill="none" stroke="#fff" stroke-width="1.5"/></svg></div>
<div class="abs contact-icon" style="left:947px;top:3364px"><svg width="40" height="40" viewBox="0 0 40 40"><path d="M6 5c4-3 7 3 8 6s-3 4-2 7 6 8 9 9 4-3 7-2 8 4 5 8-12 2-20-6S2 8 6 5z" fill="none" stroke="#fff" stroke-width="2"/></svg></div>
<div class="abs contact-info" style="left:123px;top:3460px">Email:<br>hello@pelmora.co.nz</div>
<div class="abs contact-info" style="left:465px;top:3460px">412 Harbour Lane,<br>Kelmont, 0631, Auckland</div>
<div class="abs contact-info" style="left:840px;top:3462px">Phone:<br>021 00 47 19</div>

<div class="abs field" style="left:176px;top:3561px;width:430px">&#9679; First Name</div>
<div class="abs field" style="left:623px;top:3561px;width:430px">&#9679; Last Name</div>
<div class="abs field" style="left:176px;top:3616px;width:430px">&#9632; Zipcode</div>
<div class="abs field" style="left:176px;top:3671px;width:430px">&#9633; Email Address</div>
<div class="abs field" style="left:176px;top:3727px;width:430px">&#9742; Phone Number</div>
<div class="abs field" style="left:623px;top:3616px;width:430px;height:150px">&#9679; Message :</div>
<div class="abs btn submit">SUBMIT <span class="arrow"></span></div>

<footer class="abs footer" role="img" aria-label="Dim photo of a team meeting around a table"></footer>
<svg class="abs" style="left:0;top:3972px" width="1200" height="90" viewBox="0 0 1200 90">
  <path d="M0 0 L1200 0 L1200 10 Q600 110 0 10 Z" fill="#111"/>
  <path d="M0 0 L1200 0 L1200 6 Q600 92 0 6 Z" fill="#fff"/>
</svg>
<div class="abs footer-brand">Pelmora</div>
<div class="abs footer-social"><span></span><span></span><span></span><span></span></div>
<div class="abs footer-nav" style="top:4292px">HOME<i>|</i>ABOUT US<i>|</i>OUR SERVICES<i>|</i>MY QUOTE<i>|</i>CONTACT US</div>
<div class="abs footer-nav" style="top:4340px;font-size:15px;font-weight:400">PRIVACY POLICY<i>|</i>TERMS OF USE<i>|</i>DISCLAIMER<i>|</i>SUPPORT</div>
<div class="abs copy">© 2019 Pelmora. All Right Reserved</div>

</body>
</html>
```